Tallpine Facility Upkeep Systems

I need a full website built that must work on destkop and mobile. I have the logo's and will upload them however some stock industrial photos will be required. I will be hosting it on wix/godaddy for use with dynamics 365. Pretty simple requirements:

*Splash page
*What We Do
*How We do it
*Who Are We?
*Software
*Partnerships
*Contact: Includes twitter/insta and email/addy/phone

The site should be more scroll oriented with fewer tabs to allow for a improved mobile experience.
We're also looking for ways to improve our inbound marketing and would want to include various areas to get in touch /or collect their info. Look to www.kelnarova.com as an example of inbound marketing.
Images should be representative of the verticals we're focused on.

I have most of the content.

Target Market(s)

Asset intensive industries: Mining, Oil and Gas, Forest Products and Manufacturing.

Industry/Entity Type

Asset Management

Coding

Coded - Design and coding required

Number of Pages Required

5+ page

Font styles to use
Sans Serif

Requirements
Must have
• Must be easy to view and navigate on mobile and desktop.
Nice to have
• Employee/Customer portal.
Should not have
• Anything that will not display well in a mobile environment.

```html
<!DOCTYPE html>
<html lang="en">
<head>
<meta charset="utf-8">
<title>Tallpine Facility Upkeep Systems</title>
<link rel="stylesheet" href="https://fonts.googleapis.com/css2?family=Mulish:wght@300;400;700&display=swap">
<style>
  :root {
    --brand-green: #45920a;
    --panel-green: rgba(78, 154, 22, 0.86);
    --ink-navy: #1f2450;
    --white: #ffffff;
    --sky-top: #6f8da3;
    --sky-mid: #b7c3c4;
    --sky-warm: #d9a27c;
    --sky-low: #e4a067;
    --steel-dark: #1c1c1c;
  }
  * { margin: 0; padding: 0; box-sizing: border-box; }
  html, body { width: 1200px; height: 658px; overflow: hidden; }
  body { font-family: "Mulish", sans-serif; color: var(--white); position: relative; background: var(--sky-top); }

  .hero-photo {
    position: absolute; inset: 0;
    background:
      linear-gradient(90deg, rgba(28,28,28,0) 0%, rgba(28,28,28,0) 55%, rgba(28,28,28,0.35) 68%, rgba(28,28,28,0.2) 100%),
      linear-gradient(180deg, var(--sky-top) 0%, #8fa8b6 22%, var(--sky-mid) 40%, var(--sky-warm) 62%, var(--sky-low) 76%, #4a3a32 88%, var(--steel-dark) 100%);
  }

  .nav-band {
    position: absolute; left: 0; top: 38px; width: 1200px; height: 37px;
    background: var(--brand-green);
  }
  .main-nav {
    position: absolute; top: 38px; right: 34px; height: 37px;
    display: flex; align-items: center; gap: 20px;
    list-style: none; font-size: 12.5px; font-weight: 400; letter-spacing: 0.2px;
  }
  .main-nav li:nth-child(2) { margin-right: 4px; }

  .logo-card {
    position: absolute; left: 84px; top: 0; width: 260px; height: 106px;
    background: var(--white);
    display: flex; align-items: center; justify-content: center;
  }
  .logo-name { font-size: 24px; font-weight: 400; color: var(--ink-navy); line-height: 1; }

  .intro-panel {
    position: absolute; left: 86px; top: 246px; width: 534px; height: 247px;
    background: var(--panel-green);
    border: 1px solid rgba(255,255,255,0.25);
    padding: 24px 32px 0 32px;
  }
  .intro-title { font-size: 30px; font-weight: 300; line-height: 1.1; margin-bottom: 22px; }
  .intro-copy { max-width: 450px; font-size: 13.5px; font-weight: 300; line-height: 16.8px; margin-bottom: 16px; }
  .intro-link { display: inline-block; margin-top: -3px; font-size: 13.5px; font-weight: 700; color: var(--white); text-decoration: none; }
</style>
</head>
<body>
  <div class="hero-photo" role="img" aria-label="Silhouetted construction workers on scaffolding guiding a suspended concrete bucket against a dusk sky"></div>

  <div class="nav-band"></div>
  <ul class="main-nav">
    <li>HOME</li>
    <li>WHAT WE DO</li>
    <li>SERVICES</li>
    <li>CONTACT</li>
  </ul>

  <div class="logo-card">
    <div class="logo-name">Tallpine Upkeep</div>
  </div>

  <section class="intro-panel">
    <h1 class="intro-title">What is Tallpine Upkeep</h1>
    <p class="intro-copy">Tallpine facility upkeep systems is a boutique firm specializing in maintenance and reliability, supply chain, business intelligence and program management for asset intensive industries.</p>
    <p class="intro-copy">We represent the finest people, process and technology tools to achieve greater results.</p>
    <a class="intro-link" href="#">Learn more &gt;</a>
  </section>
</body>
</html>
```